Glamour By Tavi

I am a makeup artist looking for professional looking double sided business card. I would like to create a logo and incorporate a set of eyes as the periods above the name "Tavi" on the card.

front of card: Logo "Glamour by Tavi" written across diagonal (bottom left to top right)

Back of card:
1) Professional makeup artist serving New York & New Jersey (or similar to this text)
2) 917-555-0148
3) glamourbytavi@mailcove.com

Industry/Entity Type

Business

```html
<!DOCTYPE html>
<html lang="en">
<head>
<meta charset="utf-8">
<title>Glamour by Tavi – Business Card</title>
<link rel="stylesheet" href="https://fonts.googleapis.com/css2?family=Parisienne&display=swap">
<style>
  :root {
    --backdrop: #e9e9ea;
    --blush: #f2d3c6;
    --blush-light: #f7e3da;
    --paper: #ffffff;
    --ink: #1a1414;
    --shadow: rgba(60, 50, 50, 0.18);
    --eye-lilac: #c9b3cf;
    --eye-rose: #e8c4b8;
  }
  * { margin: 0; padding: 0; box-sizing: border-box; }
  html, body {
    width: 1200px;
    height: 902px;
    overflow: hidden;
    background: var(--backdrop);
  }
  .stage {
    position: relative;
    width: 1200px;
    height: 902px;
    display: flex;
    align-items: center;
    justify-content: center;
    gap: 60px;
  }
  .card {
    position: relative;
    width: 520px;
    height: 300px;
    overflow: hidden;
    box-shadow: 0 10px 28px var(--shadow);
    font-family: "Parisienne", cursive;
    color: var(--ink);
  }
  .card--front {
    background: linear-gradient(160deg, var(--blush) 0%, var(--blush-light) 30%, var(--paper) 75%);
  }
  .brand-name {
    position: absolute;
    left: 50%;
    top: 50%;
    transform: translate(-50%, -50%) rotate(-32deg);
    font-size: 66px;
    font-weight: 400;
    white-space: nowrap;
    color: var(--ink);
  }
  .card--back {
    background: var(--blush);
  }
  .eye-visual {
    position: absolute;
    left: 0;
    top: 70px;
    width: 300px;
    height: 230px;
    background:
      radial-gradient(ellipse 55% 40% at 45% 50%, var(--eye-lilac) 0%, var(--eye-rose) 55%, rgba(242, 211, 198, 0) 100%);
  }
  .contact {
    position: absolute;
    right: 24px;
    top: 34px;
    width: 280px;
    text-align: center;
    line-height: 1.15;
  }
  .contact__tagline { font-size: 26px; }
  .contact__region { font-size: 30px; margin-top: 4px; }
  .contact__phone { font-size: 30px; margin-top: 34px; }
  .contact__email { font-size: 20px; margin-top: 24px; }
</style>
</head>
<body>
  <main class="stage">
    <section class="card card--front" aria-label="Card front">
      <p class="brand-name">Glamour by Tavi</p>
    </section>
    <section class="card card--back" aria-label="Card back">
      <div class="eye-visual" role="img" aria-label="Soft close-up of an eye with lavender and rose eyeshadow"></div>
      <div class="contact">
        <p class="contact__tagline">Professional makeup artist<br>serving</p>
        <p class="contact__region">New York &amp; New Jersey</p>
        <p class="contact__phone">917-555-0148</p>
        <p class="contact__email">glamourbytavi@mailcove.com</p>
      </div>
    </section>
  </main>
</body>
</html>
```